Vent doux

Hello,
I’m a designer sunglasses reatail Store owner in Montreal, Quebec.

Looking for something modern, fresh with a trendy appeal.

Will send my logo.
Thank you.

Store

```html
<!DOCTYPE html>
<html lang="fr">
<head>
<meta charset="utf-8">
<title>Vent Doux – cartes de visite</title>
<link rel="stylesheet" href="https://fonts.googleapis.com/css2?family=Open+Sans:wght@400;600&family=Michroma&display=swap">
<style>
  :root {
    --backdrop: #161c24;
    --card: #f1f1f3;
    --band: #ffffff;
    --ink: #1e1e22;
    --muted: #3a3a40;
    --accent: #c8222a;
  }
  * { box-sizing: border-box; margin: 0; padding: 0; }
  html, body {
    width: 1200px; height: 800px; overflow: hidden;
    background: var(--backdrop);
  }
  .sheet {
    width: 1200px; height: 800px;
    display: flex; flex-direction: column; align-items: center; justify-content: center;
    gap: 28px;
  }
  .card {
    position: relative;
    width: 640px; height: 366px;
    background: var(--card);
    border-top: 26px solid var(--band);
    border-bottom: 26px solid var(--band);
    font-family: "Open Sans", sans-serif;
    color: var(--ink);
  }
  .brand { display: flex; flex-direction: column; }
  .brand-row { display: flex; align-items: center; gap: 14px; }
  .brand-dot { border-radius: 50%; background: var(--accent); flex: none; }
  .brand-name {
    font-family: "Michroma", sans-serif;
    font-weight: 400; text-transform: uppercase; color: var(--ink);
    line-height: 1;
  }
  .brand-tagline {
    font-family: "Michroma", sans-serif;
    color: var(--muted); letter-spacing: 0.14em;
  }

  /* front */
  .card--front { display: flex; align-items: center; justify-content: center; }
  .card--front .brand-dot { width: 44px; height: 44px; }
  .card--front .brand-name { font-size: 40px; letter-spacing: 0.02em; }
  .card--front .brand-tagline { font-size: 15px; margin: 10px 0 0 58px; }

  /* back */
  .card--back { display: flex; align-items: center; padding: 0 20px 0 24px; justify-content: space-between; }
  .card--back .brand-row { gap: 9px; }
  .card--back .brand-dot { width: 24px; height: 24px; }
  .card--back .brand-name { font-size: 21px; }
  .card--back .brand-tagline { font-size: 8.5px; margin: 6px 0 0 33px; }
  .contact { list-style: none; display: flex; flex-direction: column; gap: 14px; font-size: 16px; letter-spacing: 0.02em; }
  .contact li { display: flex; align-items: flex-start; gap: 12px; line-height: 1.2; }
  .contact svg { width: 14px; height: 14px; margin-top: 3px; flex: none; }
</style>
</head>
<body>
<main class="sheet">
  <section class="card card--front" aria-label="Recto">
    <div class="brand">
      <div class="brand-row">
        <span class="brand-dot"></span>
        <span class="brand-name">Vent Doux</span>
      </div>
      <span class="brand-tagline">lunettes &amp; accessoires</span>
    </div>
  </section>

  <section class="card card--back" aria-label="Verso">
    <div class="brand">
      <div class="brand-row">
        <span class="brand-dot"></span>
        <span class="brand-name">Vent Doux</span>
      </div>
      <span class="brand-tagline">lunettes &amp; accessoires</span>
    </div>
    <ul class="contact">
      <li>
        <svg viewBox="0 0 14 14" aria-hidden="true"><rect x="0.5" y="0.5" width="13" height="13" rx="2" fill="none" stroke="#1e1e22"/><circle cx="7" cy="5.5" r="2" fill="#1e1e22"/><path d="M3.5 11c.5-2 2-3 3.5-3s3 1 3.5 3z" fill="#1e1e22"/></svg>
        <span>Boutique Vent Doux</span>
      </li>
      <li>
        <svg viewBox="0 0 14 14" aria-hidden="true"><rect x="0.5" y="0.5" width="13" height="13" rx="2" fill="none" stroke="#1e1e22"/><path d="M7 12c-2-2.5-3-4-3-5.5a3 3 0 0 1 6 0C10 8 9 9.5 7 12z" fill="none" stroke="#1e1e22" stroke-width="1.2"/><circle cx="7" cy="6.4" r="1" fill="#1e1e22"/></svg>
        <span>418 Rue des Érables<br>Montreal, Quebec H3k2p4</span>
      </li>
      <li>
        <svg viewBox="0 0 14 14" aria-hidden="true"><rect x="0.5" y="0.5" width="13" height="13" rx="2" fill="none" stroke="#1e1e22"/><path d="M5 3h2l.5 2.5-1.2.8c.5 1.2 1.2 2 2.4 2.5l.8-1.2L12 8v2c-4.5.5-8-3-7-7z" fill="#1e1e22" transform="translate(-1 0)"/></svg>
        <span>514 555-0142</span>
      </li>
      <li>
        <svg viewBox="0 0 14 14" aria-hidden="true"><rect x="0.5" y="0.5" width="13" height="13" rx="2" fill="none" stroke="#1e1e22"/><rect x="3" y="4.5" width="8" height="5.5" fill="none" stroke="#1e1e22"/><path d="M3 4.5l4 3 4-3" fill="none" stroke="#1e1e22"/></svg>
        <span>bonjour@ventdoux.ca</span>
      </li>
    </ul>
  </section>
</main>
</body>
</html>
```